Redesign www.brillorackets.com

I want a website designer to design my website for me. There is a site up right now but it's not complete because my clients can not pay for my services online. Whoever signs up for this project will have to work on a speedy schedule to be able to complete the new site within a week. I have all of the information online so now at www.brillorackets.com I can send you other files as well. Please let me know if you will be able to do this.

The site needs to be optimize for all platforms like, desktop, laptop, and smartphone.

I do have a paypal account that we can link to the site to accept transactions.

Thank you,

Tomas

Target Market(s)

Tennis players

Coding

Coded - Design and coding required

Number of Pages Required

5+ page

Font styles to use
Sans Serif
Script

Colors
00a990
a4ce38
ffffff
fbee3f

Requirements
Must have
• Ability to read through the site and ensure that the functionality works. Must have some testing and QA background in order to perform thorough testing and quality assurance prior to delivery. I will prefer a WordPress template for the site.
Nice to have
• Not sure if I will need my own merchant account, but if that's the case, I can get one.

```html
<!DOCTYPE html>
<html lang="en">
<head>
<meta charset="utf-8">
<title>Vantrel Tennis &amp; Racket Services</title>
<link href="https://fonts.googleapis.com/css2?family=Roboto:wght@300;400;500;700&display=swap" rel="stylesheet">
<style>
:root{
  --navy:#1b2030;
  --navy-2:#232a3b;
  --green:#84c441;
  --lime:#c8dc2e;
  --ink:#222;
  --muted:#8a8a8a;
  --panel:#efefef;
  --card:#f3f3f3;
  --white:#fff;
}
*{box-sizing:border-box;margin:0;padding:0}
html,body{width:1200px;height:3396px;overflow:hidden}
body{font-family:"Roboto",Arial,sans-serif;color:var(--ink);background:var(--white);position:relative}
.abs{position:absolute}
.btn{display:flex;align-items:center;justify-content:center;background:var(--green);color:var(--white);font-weight:700;text-transform:uppercase;font-size:19px;letter-spacing:.5px}

/* header */
.site-header{position:absolute;left:0;top:0;width:1200px;height:200px;background:var(--navy)}
.brand{position:absolute;left:66px;top:22px;display:flex;align-items:center;gap:14px}
.brand-dot{width:46px;height:46px;border-radius:50%;background:var(--green)}
.brand-name{font-size:40px;font-weight:700;color:var(--green);letter-spacing:1px}
.signup{position:absolute;left:408px;top:0;width:420px;height:42px;background:var(--lime);clip-path:polygon(0 0,100% 0,94% 100%,0 100%);color:var(--white);font-size:18px;display:flex;align-items:center;padding-left:66px;gap:16px}
.search{position:absolute;left:815px;top:0;width:317px;height:42px;background:#0f131d;color:#fff;font-size:17px;display:flex;align-items:center;justify-content:space-between;padding:0 22px 0 24px}
.contact-line{position:absolute;top:78px;left:480px;display:flex;align-items:center;color:var(--green);font-size:20px}
.contact-line span{color:#d6e9b0}
.contact-line .sep{width:1px;height:36px;background:#4a5266;margin:0 30px}
.main-nav{position:absolute;left:0;top:140px;width:1200px;height:60px;background:var(--navy-2);display:flex;align-items:center;padding-left:66px}
.main-nav a{color:#fff;text-decoration:none;font-size:16px;margin-right:62px}

/* hero */
.hero{position:absolute;left:0;top:200px;width:1200px;height:475px;background:linear-gradient(100deg,#3d4a3a 0%,#5b6f4e 35%,#8a9b84 65%,#6a7c62 100%)}
.hero-copy{position:absolute;left:66px;top:86px;color:#fff}
.hero-copy h1{font-weight:300;font-size:70px;line-height:88px}
.hero-copy p{font-size:21px;text-transform:uppercase;margin-top:2px}
.hero .btn{position:absolute;left:66px;top:320px;width:162px;height:42px;font-size:17px;text-transform:none}
.slide-arrow{position:absolute;top:222px;width:36px;height:36px;border-radius:50%;border:2px solid rgba(255,255,255,.5)}

/* welcome */
.welcome{position:absolute;left:0;top:675px;width:1200px;height:510px;background:var(--panel)}
.welcome-photo{position:absolute;left:66px;top:79px;width:500px;height:353px;background:linear-gradient(135deg,#e8b2c2,#7e8d6a)}
.welcome-box{position:absolute;left:548px;top:45px;width:584px;height:412px;background:#fff;text-align:center;padding:28px 40px}
.welcome-box h2{font-weight:400;font-size:38px;letter-spacing:2px}
.welcome-box p{color:var(--muted);font-size:19px;line-height:27px;margin-top:16px}
.welcome-box .btn{width:214px;height:50px;margin:22px auto 0}

/* services */
.section-title{font-weight:400;font-size:38px;text-align:center;letter-spacing:1px}
.services{position:absolute;left:0;top:1185px;width:1200px;height:717px}
.services .section-title{margin-top:44px}
.service-card{position:absolute;top:121px;width:337px;height:524px;background:var(--card)}
.service-img{height:226px;display:flex;align-items:center;justify-content:center;color:#fff;font-size:36px;font-weight:300;text-align:center;line-height:40px}
.service-card ul{padding:30px 22px 0 48px;font-size:15px;color:#555;line-height:21px}
.service-card li{margin-bottom:16px}
.service-card ul.small{font-size:12px;line-height:14px;padding-top:22px}
.service-card ul.small li{margin-bottom:14px}
.service-card .btn{position:absolute;left:82px;top:445px;width:178px;height:52px}

/* coaches */
.coaches{position:absolute;left:0;top:1902px;width:1200px;height:781px;background:linear-gradient(160deg,#2c3340,#1e2430 55%,#39414c)}
.coaches .section-title{color:#fff;margin-top:50px}
.coach{position:absolute;width:514px;height:212px;background:#fff;display:flex}
.coach-photo{width:186px;height:212px;flex:none}
.coach-body{padding:22px 18px 0;text-align:center;flex:1}
.coach-body h3{font-weight:400;font-size:23px;letter-spacing:.5px}
.coach-body .role{color:#3f9a3f;font-size:13px;margin:6px 0 10px}
.coach-body p{color:var(--muted);font-size:12.5px;line-height:17px}
.coaches .btn{position:absolute;left:482px;top:663px;width:236px;height:58px}

/* testimonial */
.story{position:absolute;left:0;top:2683px;width:1200px;height:419px}
.story .section-title{margin-top:52px}
.quote{position:absolute;left:150px;top:142px;width:900px;text-align:center;color:#555;font-size:23px;line-height:32px}
.qmark{position:absolute;font-size:58px;color:#777;line-height:1}
.author{position:absolute;left:776px;top:282px;font-size:30px;color:#555}
.author-role{position:absolute;left:776px;top:322px;font-size:27px;color:#4a9a2f;font-style:italic}

/* footer */
.site-footer{position:absolute;left:0;top:3102px;width:1200px;height:226px;background:var(--navy)}
.foot-left{position:absolute;left:250px;top:110px;color:#fff;font-size:14px;line-height:22px;text-align:right}
.foot-right{position:absolute;left:808px;top:110px;color:#fff;font-size:14px;line-height:22px}
.foot-brand{position:absolute;left:490px;top:86px;display:flex;align-items:center;gap:12px}
.copyright{position:absolute;left:0;top:3328px;width:1200px;height:68px;background:#121620;color:#cfd3dc;font-size:15px;display:flex;align-items:center;justify-content:center}
</style>
</head>
<body>

<header class="site-header">
  <div class="brand"><span class="brand-dot"></span><span class="brand-name">Vantrel</span></div>
  <div class="signup">
    <svg width="16" height="16" viewBox="0 0 16 16"><circle cx="8" cy="5" r="4" fill="#fff"/><path d="M1 16c0-4 3-6 7-6s7 2 7 6z" fill="#fff"/></svg>
    Sign up
  </div>
  <div class="search">Search.......
    <svg width="18" height="18" viewBox="0 0 18 18"><circle cx="7" cy="7" r="5.5" stroke="#fff" stroke-width="2" fill="none"/><path d="M11 11l6 6" stroke="#fff" stroke-width="2"/></svg>
  </div>
  <div class="contact-line">
    <svg width="22" height="22" viewBox="0 0 24 24"><path d="M6.6 10.8a15 15 0 006.6 6.6l2.2-2.2a1 1 0 011-.25 11.4 11.4 0 003.6.57 1 1 0 011 1V20a1 1 0 01-1 1A17 17 0 013 4a1 1 0 011-1h3.5a1 1 0 011 1c0 1.25.2 2.45.57 3.57a1 1 0 01-.25 1z" fill="currentColor"/></svg>
    <span style="margin-left:12px">555-214-0387</span>
    <span class="sep"></span>
    <svg width="18" height="24" viewBox="0 0 18 24"><path d="M9 0a9 9 0 019 9c0 6-9 15-9 15S0 15 0 9a9 9 0 019-9z" fill="currentColor"/><circle cx="9" cy="9" r="3.4" fill="#1b2030"/></svg>
    <span style="margin-left:14px">Play Like A Champion Westbridge, VA 22000</span>
  </div>
  <nav class="main-nav">
    <a>Home</a><a>About</a><a>Our Services</a><a>Our Team</a><a>Gallery</a><a>Summer Camp</a><a>Blog</a><a>Contact us</a>
  </nav>
</header>

<section class="hero" role="img" aria-label="Photo of a tennis player reaching up to serve on an outdoor court">
  <div class="hero-copy">
    <h1>The more you<br>sweat in training</h1>
    <p>The less you lose in matches</p>
  </div>
  <a class="btn">Book Lessons</a>
  <span class="slide-arrow" style="left:22px"></span>
  <span class="slide-arrow" style="right:22px"></span>
</section>

<section class="welcome">
  <div class="welcome-photo" role="img" aria-label="Photo of two young players in pink shirts holding rackets"></div>
  <div class="welcome-box">
    <h2>WELCOME</h2>
    <p>Vantrel Tennis &amp; Racket Services activities (Lessons, Clinics, Team Practices, Video Analysis, Tournaments, etc) are run under the direction and leadership of Master Tennis Coach - Tomas Velder. Tomas is a well-known in tennis around the Northern Virginia Area. He has vast experience at teaching all levels of tennis, from the quick starter to touring professionals.</p>
    <a class="btn">Learn More</a>
  </div>
</section>

<section class="services">
  <h2 class="section-title">OUR SERVICES</h2>
  <article class="service-card" style="left:66px">
    <div class="service-img" role="img" aria-label="Photo of a racket and tennis ball" style="background:linear-gradient(135deg,#7a6a5a,#b9b13a)">TENNIS<br>LESSONS</div>
    <ul>
      <li>Private Lesson: 1:1 ratio | Cost: $85 per hour</li>
      <li>Semi-Private Lesson: 2:1 ratio | Cost (per person): $45 per hour</li>
      <li>Group Clinic: 3 or more players | Cost (per person): $25 per hour</li>
    </ul>
    <a class="btn">Book Now</a>
  </article>
  <article class="service-card" style="left:432px">
    <div class="service-img" role="img" aria-label="Photo of a group of young players on court" style="background:linear-gradient(135deg,#9a5a6a,#6c7a5c)">TENNIS<br>DRILLS</div>
    <ul>
      <li>Single</li>
      <li style="margin-top:30px">Double</li>
    </ul>
    <a class="btn">Book Now</a>
  </article>
  <article class="service-card" style="left:797px">
    <div class="service-img" role="img" aria-label="Photo of a coach with a camper" style="background:linear-gradient(135deg,#4b3a2e,#8e8a7a)">SUMMER<br>CAMP 2016</div>
    <ul class="small">
      <li>Full Day Summer Camp 2016 Package - Discounts Apply ! Buy Now and Get Additional 10% off</li>
      <li>Half Day Summer Camp 2016 Package - Discounts Apply ! Buy Now and Get Additional 10% off</li>
      <li>Drop Off Half Day Session Summer Camp 2016 Package - Discounts Apply ! Buy 3 or more days and get 10% off</li>
      <li>Drop Off Full Day Session Summer Camp 2016 Package - Discounts Apply ! Buy 3 or more days and get 10% off</li>
    </ul>
    <a class="btn">Book Now</a>
  </article>
</section>

<section class="coaches" role="group" aria-label="Our club coaches">
  <h2 class="section-title">OUR CLUB COACHES</h2>
  <article class="coach" style="left:66px;top:129px">
    <div class="coach-photo" role="img" aria-label="Portrait of the head coach" style="background:linear-gradient(160deg,#7aa05a,#e8742a)"></div>
    <div class="coach-body"><h3>TOMAS O. VELDER</h3><div class="role">Owner and Master of Tennis</div>
      <p>Tomas Velder is a "Certified Master of Tennis - Performance" with the National Coaching Registry (NCR). This qualification program is equivalent to World Tennis Council's (WTC) Level 3 Certificate.</p></div>
  </article>
  <article class="coach" style="left:618px;top:129px">
    <div class="coach-photo" role="img" aria-label="Portrait of the camp counselor" style="background:linear-gradient(160deg,#b7a07a,#6b4a32)"></div>
    <div class="coach-body"><h3>MAYA VELDER</h3><div class="role">Camp Counselor</div>
      <p>Maya Velder is the second oldest daughter of Tomas Velder. She is 16 years old and a sophomore at Westbridge High School where she plays #1 for the team. This year she was 13-3. She lost twice to Valerie Hollis of Ridgeview and once to Lexi Corbin of Parkdale.</p></div>
  </article>
  <article class="coach" style="left:66px;top:398px">
    <div class="coach-photo" role="img" aria-label="Portrait of a camp coach" style="background:linear-gradient(160deg,#4f6a3e,#c49a80)"></div>
    <div class="coach-body"><h3>LIA MARSTEN</h3><div class="role">Camp coach</div>
      <p>Lia Marsten is a dedicated educator of physical education in sports with more than ten years of experience under her belt. She will be helping us with all of the campers as assistant to Tomas Velder.</p></div>
  </article>
  <article class="coach" style="left:618px;top:398px">
    <div class="coach-photo" role="img" aria-label="Portrait of a camp coach" style="background:linear-gradient(160deg,#8a6a4a,#2e4a8a)"></div>
    <div class="coach-body"><h3>SAMMY ORREN</h3><div class="role">Camp Coach</div>
      <p>Sammy Orren has been playing tennis for over 25 years. Coach Sammy loved coaching from the very beginning of being introduced to tennis. Since,</p></div>
  </article>
  <a class="btn">View More</a>
</section>

<section class="story">
  <h2 class="section-title">CLIENT SUCCESS STORY</h2>
  <span class="qmark" style="left:130px;top:132px">&ldquo;</span>
  <p class="quote">You've taken everyone's kids a very long way on this road to success and their lives are much the better for it. They showed everyone what the results of working with a stellar coach look like. Many, many thanks to you Tomas.</p>
  <span class="qmark" style="left:875px;top:218px">&rdquo;</span>
  <div class="author">-Dr. Jules Marrow</div>
  <div class="author-role">Parent</div>
</section>

<footer class="site-footer">
  <div class="foot-left">Play Like A Champion<br>Westbridge, VA 22000</div>
  <svg class="abs" style="left:430px;top:118px" width="14" height="20" viewBox="0 0 18 24"><path d="M9 0a9 9 0 019 9c0 6-9 15-9 15S0 15 0 9a9 9 0 019-9z" fill="#fff"/><circle cx="9" cy="9" r="3.4" fill="#1b2030"/></svg>
  <div class="foot-brand"><span class="brand-dot"></span><span class="brand-name">Vantrel</span></div>
  <svg class="abs" style="left:756px;top:118px" width="18" height="18" viewBox="0 0 24 24"><path d="M6.6 10.8a15 15 0 006.6 6.6l2.2-2.2a1 1 0 011-.25 11.4 11.4 0 003.6.57 1 1 0 011 1V20a1 1 0 01-1 1A17 17 0 013 4a1 1 0 011-1h3.5a1 1 0 011 1c0 1.25.2 2.45.57 3.57a1 1 0 01-.25 1z" fill="#fff"/></svg>
  <div class="foot-right">Book a program today!<br>Call us on 555-214-0387</div>
</footer>
<div class="copyright">&copy;copyright 2017 All Rights Reserved</div>

</body>
</html>
```